We need a web design for a new hair care company that is based in Israel but exports its line of products around the world. We would like special features on this website that include video, sliders and other exciting effects. The final design should present information about the products and an exciting inviting image. We also will need to know how to update the site.

Designers can look at our current website and see the colors and look of the products as well. Please go to: http://velorintresses.com

We would like to use the colors of the Velorin Tress care line of products. Wordpress seems to be a good choice. We would like four pages: Home, About Us, Contact and Products.

If designers have specific questions.....please let us know!
Let the designs begin!!!!
We are waiting and excited!

Target Market(s)

Potential haircare distributors and general public

Industry/Entity Type

Hair

Requirements
Must have
• The website must have general info about what the company is, with a video, explain how to use each product and a focus on women and hair.
Nice to have
• On the website should be the logo, product info, upbeat music, video and sliders that show the exciting world of Velorin Tresscare. It's uniqueness is that it offers Dead Sea minerals for the hair, the first of its kind.

```html
<!DOCTYPE html>
<html lang="en">
<head>
<meta charset="utf-8">
<title>Velorin Tress</title>
<link rel="stylesheet" href="https://fonts.googleapis.com/css2?family=Roboto+Condensed:wght@300;400;700&family=Roboto:wght@400&display=swap">
<style>
:root{
  --brown:#5a2a0c;
  --brown-deep:#3b1806;
  --nav-pill:#6b2a08;
  --page:#faf5ef;
  --header:#f1f1f1;
  --rule:#e3dcd3;
  --text:#4a4a4a;
  --footer:#333232;
  --orange:#e98a3a;
  --orange-light:#f6c07d;
  --cream:#f9e6cf;
}
*{margin:0;padding:0;box-sizing:border-box}
html,body{width:1200px;height:1080px;overflow:hidden}
body{background:var(--page);font-family:"Roboto",Arial,sans-serif;color:var(--text);position:relative}
.abs{position:absolute}
.cond{font-family:"Roboto Condensed",Arial,sans-serif}

.site-header{left:0;top:0;width:1200px;height:147px;background:var(--header);border-top:8px solid var(--brown);box-shadow:0 1px 3px rgba(0,0,0,.12)}
.brand{left:120px;top:48px;display:flex;align-items:center;gap:12px;font-family:"Roboto Condensed",sans-serif;font-weight:400;font-size:44px;color:var(--brown)}
.brand-dot{width:26px;height:26px;border-radius:50%;background:var(--brown)}

.player{left:511px;top:0;width:419px;height:43px;background:var(--brown);color:#fff;font-size:11px}
.player .track{left:14px;top:8px;line-height:14px}
.player .artist{color:#b8907a;font-size:10px}
.player .ctrls{left:170px;top:7px;display:flex;gap:10px;align-items:center}
.ctrl-box{width:18px;height:16px;border-radius:2px;background:#1e0c03}
.ctrl-wide{width:30px}
.transport{left:324px;top:0;width:84px;height:40px;display:flex;align-items:center;justify-content:center;gap:2px}
.btn-round{width:22px;height:22px;border-radius:50%;background:#222;border:2px solid #555}
.btn-round.big{width:32px;height:32px}
.lang{left:941px;top:0;width:139px;height:43px;background:var(--brown)}
.lang .box{left:10px;top:10px;width:118px;height:26px;background:#fff;border:1px solid #ccc;font-family:"Roboto Condensed",sans-serif;font-weight:700;font-size:13px;color:#555;padding:6px 10px}
.lang .caret{left:96px;top:9px;width:0;height:0;border-left:5px solid transparent;border-right:5px solid transparent;border-top:8px solid #bbb}

.nav a{position:absolute;top:90px;height:30px;line-height:30px;font-family:"Roboto Condensed",sans-serif;font-weight:700;font-size:14px;color:#222;text-decoration:none;text-align:center}
.nav .active{left:606px;width:90px;background:var(--nav-pill);color:#fff;border-radius:15px}

.hero{left:120px;top:167px;width:960px;height:383px;background:linear-gradient(90deg,#8a4a26 0%,#c98a5e 25%,#e9c4a0 50%,#f3dcc0 70%,#f1d6b5 100%)}
.hero-title{right:22px;top:96px;text-align:right;font-family:"Roboto Condensed",sans-serif;font-weight:700;font-size:36px;line-height:43.5px;color:var(--brown-deep);letter-spacing:-.2px}
.dots{left:878px;top:352px;display:flex;gap:9px}
.dots span{width:12px;height:12px;border-radius:50%;background:#c7a58d}
.dots span.on{background:#b9b2ac}

.rule{left:120px;width:960px;height:1px;background:var(--rule)}

.ribbon{left:120px;top:593px}
.ribbon-label{left:22px;top:15px;font-family:"Roboto Condensed",sans-serif;font-weight:300;font-size:30px;color:var(--brown)}
.intro{left:360px;top:592px;width:719px;font-size:12px;line-height:18px;text-align:justify}

h2.sec{font-family:"Roboto Condensed",sans-serif;font-weight:400;font-size:24px;color:var(--brown);top:700px}
.welcome-text{left:120px;top:748px;width:300px;font-size:12px;line-height:18px;text-align:justify}
.welcome-text p+p{margin-top:18px}

.video-frame{left:450px;top:748px;width:300px;height:238px;background:#fff;box-shadow:0 1px 4px rgba(0,0,0,.25)}
.video-still{left:9px;top:9px;width:282px;height:221px;background:linear-gradient(120deg,#f4f0ec 0%,#b07d62 40%,#6e3f2a 70%,#e9e4df 100%)}
.play{left:118px;top:85px;width:66px;height:66px;border-radius:50%;background:#1c1410}
.play::after{content:"";position:absolute;left:25px;top:19px;border-top:14px solid transparent;border-bottom:14px solid transparent;border-left:22px solid #c98a4a}

.promo{left:775px;top:701px;width:305px;height:280px;border-radius:5px;overflow:hidden;background:linear-gradient(135deg,#d8661a 0%,#f08a2e 35%,#c9581a 65%,#e7b58a 100%)}
.promo-photo{left:120px;top:0;width:185px;height:280px;background:linear-gradient(90deg,rgba(240,200,150,0) 0%,rgba(240,205,160,.75) 45%,#e8c79c 100%)}
.promo-text{left:13px;top:58px;color:#fff;font-family:"Roboto Condensed",sans-serif;font-size:36px;line-height:43px;text-shadow:0 1px 2px rgba(0,0,0,.35)}
.promo-text .light{font-weight:300}
.promo-text .bold{font-weight:700}
.cta{left:16px;top:221px;width:244px;height:41px;border-radius:4px;background:linear-gradient(90deg,#fbefe0,#f3d0a8);font-family:"Roboto Condensed",sans-serif;font-size:24px;color:var(--brown-deep);padding:6px 13px;box-shadow:0 1px 3px rgba(0,0,0,.3)}

.site-footer{left:0;top:1011px;width:1200px;height:69px;background:var(--footer)}
.copy{left:120px;top:25px;font-family:"Roboto Condensed",sans-serif;font-weight:700;font-size:12px;color:#fff}
.social{left:923px;top:15px;display:flex;gap:10px}
.social span{width:32px;height:32px;border-radius:50%;background:#fff}
</style>
</head>
<body>

<header class="site-header abs">
  <div class="brand abs"><span class="brand-dot"></span>Velorin</div>
</header>

<div class="player abs" aria-label="Music player">
  <div class="track abs">♫ Golden Hours<br><span class="artist">Lena Marrow</span></div>
  <div class="ctrls abs"><span class="ctrl-box"></span><span class="ctrl-box"></span><span class="ctrl-box"></span><span class="ctrl-box ctrl-wide"></span></div>
  <div class="transport abs"><span class="btn-round"></span><span class="btn-round big"></span><span class="btn-round"></span></div>
</div>
<div class="lang abs">
  <div class="box abs">ENGLISH<span class="caret abs"></span></div>
</div>

<nav class="nav">
  <a class="active" href="#">HOME</a>
  <a href="#" style="left:730px;width:80px">ABOUT US</a>
  <a href="#" style="left:860px;width:82px">PRODUCTS</a>
  <a href="#" style="left:995px;width:72px">CONTACT</a>
</nav>

<section class="hero abs" role="img" aria-label="Slider photo of a woman with long curly auburn hair">
  <h1 class="hero-title abs">OFFERING DEAD SEA MINERALS<br>FOR THE HAIR,<br>THE FIRST OF ITS KIND</h1>
  <div class="dots abs"><span></span><span></span><span class="on"></span></div>
</section>

<div class="rule abs" style="top:568px"></div>

<div class="ribbon abs">
  <svg width="216" height="70" viewBox="0 0 216 70">
    <defs><linearGradient id="rib" x1="0" x2="1"><stop offset="0" stop-color="#e98a3a"/><stop offset="1" stop-color="#f8cf94"/></linearGradient></defs>
    <polygon points="0,0 216,0 196,35 216,70 0,70" fill="url(#rib)"/>
  </svg>
  <div class="ribbon-label abs">Our Products</div>
</div>
<p class="intro abs">Sed ut perspiciatis unde omnis iste natus error sit voluptatem accusantium doloremque laudantium, totam rem aperiam, eaque ipsa quae ab illo inventore veritatis et quasi architecto beatae vitae dicta sunt explicabo. Nemo enim ipsam voluptatem quia voluptas sit aspernatur aut odit aut fugit, sed quia consequuntur is et quasi architecto beatae vitae dicta sunt explicabo. Nemo enim ipsam voluptatem quia voluptas sit aspernatur aut odit aut fugit, sed quia consequuntur</p>

<div class="rule abs" style="top:685px"></div>

<h2 class="sec abs" style="left:120px">WELCOME!</h2>
<div class="welcome-text abs">
  <p>Sed ut perspiciatis unde omnis iste natus error sit voluptatem accusantium doloremque laudantium, totam rem aperiam, eaque ipsa quae ab illo inventore veritatis et quasi architecto beatae vitae dicta sunt explicabo. Nemo enim ipsam voluptatem quia voluptas sit aspernatur aut odit aut fugit, sed quia consequuntur magni dolores eos qui ratione voluptatem sequi nesciunt. Neque porro quisquam est, qui dolorem ipsum quia dolor sit amet, consectetur,</p>
  <p>adipisci velit, sed quia non numquam eius modi tempora incidunt ut labore et dolore magnam aliquam quaerat voluptatem.</p>
</div>

<h2 class="sec abs" style="left:452px">OUR VIDEO</h2>
<div class="video-frame abs">
  <div class="video-still abs" role="img" aria-label="Video still of a woman with long straight brown hair"></div>
  <div class="play abs" style="left:127px;top:94px"></div>
</div>

<aside class="promo abs">
  <div class="promo-photo abs" role="img" aria-label="Photo of a woman with blonde hair"></div>
  <div class="promo-text abs"><span class="light">Find Out</span><br><span class="bold">Our<br>Product</span></div>
  <div class="cta abs">Get Started Now!</div>
</aside>

<footer class="site-footer abs">
  <div class="copy abs">©2013 VELORIN TRESS. ALL RIGHTS RESERVED.</div>
  <div class="social abs" aria-label="Social links"><span></span><span></span><span></span><span></span></div>
</footer>

</body>
</html>
```